Bref créative
Bright Path Fund - Not for Profit - Stationary and Business Cards
Professional
Dale Meridew
President and Chairman of the Board
20573 Lindale Avenue #238
Alder Springs, Oregon 97154
dale.meridew@brightpathfund.org
www.brightpathfund.org
Implement colors from the logo theme.
incorporate the logo into the design.
Bright Path Fund logo - AI format

```html
<!DOCTYPE html>
<html lang="en">
<head>
<meta charset="utf-8">
<title>Bright Path Fund – Stationery Set</title>
<link href="https://fonts.googleapis.com/css2?family=Open+Sans:wght@400;700&display=swap" rel="stylesheet">
<style>
  :root {
    --brand-red: #d7262b;
    --ink: #333333;
    --ink-soft: #6b6b6b;
    --paper: #ffffff;
    --backdrop: #e9e6e1;
    --faint: #f1f1f1;
    --shadow: rgba(0,0,0,0.14);
  }
  * { box-sizing: border-box; margin: 0; padding: 0; }
  html, body { width: 1200px; height: 794px; overflow: hidden; }
  body {
    position: relative;
    background: var(--backdrop);
    font-family: "Open Sans", Arial, sans-serif;
    color: var(--ink);
  }
  .sheet {
    position: absolute;
    background: var(--paper);
    box-shadow: 0 3px 10px var(--shadow);
    overflow: hidden;
  }
  .brand {
    display: flex; align-items: center; gap: 8px;
    color: var(--brand-red); font-weight: 700; line-height: 1;
    white-space: nowrap;
  }
  .brand-dot { flex: none; border-radius: 50%; background: var(--brand-red); }
  .faint-mark { position: absolute; border-radius: 50%; background: var(--faint); }
  .contact { font-size: 8px; line-height: 1.55; color: var(--ink); white-space: nowrap; }
  .contact-row { display: flex; align-items: center; gap: 5px; }
  .contact-row svg { flex: none; }

  /* Letterhead */
  .letterhead { left: 24px; top: 24px; width: 552px; height: 749px; }
  .letterhead .brand { position: absolute; left: 30px; top: 30px; font-size: 24px; }
  .letterhead .brand-dot { width: 28px; height: 28px; }
  .letterhead .contact { position: absolute; right: 22px; top: 30px; text-align: right; }
  .letterhead .contact-row { justify-content: flex-end; }
  .letterhead .faint-mark { width: 250px; height: 250px; left: 150px; top: 340px; }

  /* Business cards */
  .card { top: 48px; width: 228px; height: 125px; border-radius: 8px; }
  .card-front { left: 631px; }
  .card-front .faint-mark { width: 110px; height: 110px; left: 18px; top: -8px; }
  .card-front .brand { position: absolute; right: 14px; top: 54px; font-size: 14px; }
  .card-front .brand-dot { width: 16px; height: 16px; }
  .card-front .web { position: absolute; right: 14px; bottom: 10px; font-size: 7px; color: var(--ink-soft); }
  .card-back { left: 876px; }
  .card-back .holder { position: absolute; right: 12px; top: 10px; text-align: right; }
  .card-back .name { font-size: 11px; font-weight: 700; color: var(--brand-red); }
  .card-back .role { font-size: 5.5px; color: var(--ink-soft); margin-bottom: 4px; }
  .card-back .contact { font-size: 5.5px; line-height: 1.6; }
  .card-back .contact-row { justify-content: flex-end; }
  .card-back .brand { position: absolute; left: 12px; bottom: 14px; font-size: 13px; }
  .card-back .brand-dot { width: 15px; height: 15px; }

  /* Envelope front */
  .envelope-front { left: 595px; top: 204px; width: 533px; height: 240px; }
  .envelope-front .brand { position: absolute; left: 24px; top: 30px; font-size: 22px; }
  .envelope-front .brand-dot { width: 26px; height: 26px; }
  .envelope-front .contact { position: absolute; left: 24px; bottom: 22px; }
  .envelope-front .faint-mark { width: 200px; height: 200px; right: 12px; top: -16px; }

  /* Envelope back */
  .envelope-back { left: 595px; top: 473px; width: 533px; height: 276px; }
  .envelope-back .flap { position: absolute; inset: 0; }
  .envelope-back .brand { position: absolute; left: 50%; top: 36px; transform: translateX(-50%); font-size: 14px; }
  .envelope-back .brand-dot { width: 16px; height: 16px; }
</style>
</head>
<body>

<svg width="0" height="0" style="position:absolute">
  <defs>
    <symbol id="icon-pin" viewBox="0 0 10 10"><path d="M5 0.5a3.2 3.2 0 0 0-3.2 3.2C1.8 6.2 5 9.5 5 9.5s3.2-3.3 3.2-5.8A3.2 3.2 0 0 0 5 0.5z" fill="#d7262b"/><circle cx="5" cy="3.7" r="1.2" fill="#fff"/></symbol>
    <symbol id="icon-phone" viewBox="0 0 10 10"><rect x="1" y="1" width="8" height="8" rx="1.5" fill="#d7262b"/><rect x="3.5" y="2.5" width="3" height="5" rx="0.6" fill="#fff"/></symbol>
    <symbol id="icon-mail" viewBox="0 0 10 10"><rect x="1" y="1" width="8" height="8" rx="1.5" fill="#d7262b"/><path d="M2.5 3.5l2.5 2 2.5-2" stroke="#fff" stroke-width="0.9" fill="none"/></symbol>
    <symbol id="icon-web" viewBox="0 0 10 10"><rect x="1" y="1" width="8" height="8" rx="1.5" fill="#d7262b"/><circle cx="5" cy="5" r="2.2" stroke="#fff" stroke-width="0.9" fill="none"/></symbol>
  </defs>
</svg>

<section class="sheet letterhead">
  <div class="brand"><span class="brand-dot"></span>Bright Path Fund</div>
  <div class="contact">
    <div class="contact-row">20573 Lindale Avenue #238, Alder Springs, Oregon 97154 <svg width="8" height="8"><use href="#icon-pin"/></svg></div>
    <div class="contact-row">(541) 555-0148 <svg width="8" height="8"><use href="#icon-phone"/></svg></div>
    <div class="contact-row">info@brightpathfund.org <svg width="8" height="8"><use href="#icon-mail"/></svg></div>
    <div class="contact-row">www.brightpathfund.org <svg width="8" height="8"><use href="#icon-web"/></svg></div>
  </div>
  <div class="faint-mark" aria-hidden="true"></div>
</section>

<section class="sheet card card-front">
  <div class="faint-mark" aria-hidden="true"></div>
  <div class="brand"><span class="brand-dot"></span>Bright Path Fund</div>
  <div class="web">www.brightpathfund.org</div>
</section>

<section class="sheet card card-back">
  <div class="holder">
    <div class="name">Dale Meridew</div>
    <div class="role">President and Chairman of the Board</div>
    <div class="contact">
      <div class="contact-row">20573 Lindale Avenue #238, Alder Springs, Oregon 97154 <svg width="6" height="6"><use href="#icon-pin"/></svg></div>
      <div class="contact-row">(541) 555-0148 <svg width="6" height="6"><use href="#icon-phone"/></svg></div>
      <div class="contact-row">dale.meridew@brightpathfund.org <svg width="6" height="6"><use href="#icon-mail"/></svg></div>
      <div class="contact-row">www.brightpathfund.org <svg width="6" height="6"><use href="#icon-web"/></svg></div>
    </div>
  </div>
  <div class="brand"><span class="brand-dot"></span>Bright Path Fund</div>
</section>

<section class="sheet envelope-front">
  <div class="faint-mark" aria-hidden="true"></div>
  <div class="brand"><span class="brand-dot"></span>Bright Path Fund</div>
  <div class="contact">
    <div class="contact-row"><svg width="8" height="8"><use href="#icon-pin"/></svg> 20573 Lindale Avenue #238</div>
    <div class="contact-row" style="padding-left:13px">Alder Springs, Oregon 97154</div>
    <div class="contact-row"><svg width="8" height="8"><use href="#icon-phone"/></svg> (541) 555-0148</div>
    <div class="contact-row"><svg width="8" height="8"><use href="#icon-mail"/></svg> info@brightpathfund.org</div>
    <div class="contact-row"><svg width="8" height="8"><use href="#icon-web"/></svg> www.brightpathfund.org</div>
  </div>
</section>

<section class="sheet envelope-back">
  <svg class="flap" width="533" height="276" viewBox="0 0 533 276" aria-hidden="true">
    <path d="M0 0 L266.5 110 L533 0" fill="none" stroke="#dedede" stroke-width="1.5"/>
    <path d="M0 276 L230 140 M533 276 L303 140" fill="none" stroke="#ececec" stroke-width="1"/>
  </svg>
  <div class="brand"><span class="brand-dot"></span>Bright Path Fund</div>
</section>

</body>
</html>
```